Website for the new investment company.

We are building a website for a new company. This will be an investment company. The name of the company is Birch Harbor Capital, or BHC. We don't have a company logo yet, so happy to take suggestions on that as well (and will add that to the final cost). The investors of this company will exclusively be Dunmore College alumni graduates. The investors are not students, but instead older professionals in various industries, that previously graduated from the Dunmore College. This company will establish an investment fund and invest in multiple businesses.
The purpose of the website will be to educate Dunmore alumni on the investment fund.
We are looking for:
1. The design to be relatable, but not the copy of the Dunmore College website. https://www.dunmorecollege-example.edu/
2. This is an investment website and must mimic other similar websites
https://quillmark-funds.com/
https://www.tallowvane.com/
https://brevinholt-group.com/site/global/home/p_home.gsp
3. Project timeline. We are focused on receiving a design in the next two weeks and then finishing the website over the following 2 weeks. We anticipate paying for additional work and customization after the designs are provided.
4. Website Pages:
1) Homepage - Mission and Objective (high quality photos along with text that we will provide after selecting the winning design)
2) Background - Text and biographies on the 2 founders (high quality photos along with text that we will provide after selecting the winning design)
3) Advisory Board - Text and biographies on the investment Fund's 3 advisory board members (high quality photos along with text that we will provide after selecting the winning design)
4) Fund I - Text and information on the specific investment fund including pictures and biographies of the investment committee (high quality photos along with text that we will provide after selecting the winning design)
5) Contact Us - Typical website contact page for visitors

Target Market(s)

Dunmore Alumni graduates

Industry/Entity Type

Investment

Coding

Coded - Design and coding required

Font styles to use
Serif
Sans Serif

Colors
0054AA
0677BA
7BADD7
CADEEF
E8F1F8

Requirements
Must have
• Must look like other private investment websites as provided in project description
Nice to have
• Mimics the Dunmore College style, but definitely needs to be different. This company has no direct relationship with Dunmore College.
Should not have
• No commercial transactions, no credit card payments etc. Do not replicate any logos, designs or proprietary content from Dunmore College.

```html
<!DOCTYPE html>
<html lang="en">
<head>
<meta charset="utf-8">
<title>Investment Company</title>
<link href="https://fonts.googleapis.com/css2?family=Lora:wght@400;700&family=Roboto:wght@400;500;700&display=swap" rel="stylesheet">
<style>
:root{
  --blue-dark:#0054AA;
  --blue:#0677BA;
  --blue-mid:#7BADD7;
  --blue-light:#CADEEF;
  --blue-pale:#E8F1F8;
  --ink:#2b2f36;
  --muted:#555b63;
  --white:#ffffff;
}
*{margin:0;padding:0;box-sizing:border-box}
html,body{width:1200px;height:2950px;overflow:hidden;background:var(--white)}
body{position:relative;font-family:'Roboto',sans-serif;color:var(--ink)}
.abs{position:absolute}
.serif{font-family:'Lora',serif}

/* header */
.site-header{position:absolute;left:0;top:0;width:1200px;height:118px;background:var(--white)}
.brand{left:111px;top:22px;font-family:'Lora',serif;font-size:29px;line-height:38px;color:var(--blue-dark);text-transform:uppercase}
.nav a{position:absolute;top:50px;font-size:15px;font-weight:500;color:#222;text-decoration:none;text-transform:uppercase}
.nav a.active{color:var(--blue);text-decoration:underline;text-underline-offset:4px}
.nav-sep{position:absolute;top:0;width:1px;height:118px;background:#e3e6ea}
.btn{position:absolute;display:flex;align-items:center;justify-content:center;background:linear-gradient(90deg,var(--blue-dark),var(--blue));color:var(--white);font-weight:500;font-size:15px;text-transform:uppercase}

/* hero */
.hero{left:0;top:118px;width:1200px;height:600px;background:linear-gradient(100deg,#6a5a4e 0%,#8c7564 30%,#a48870 55%,#c7a57f 80%,#e0c59b 100%)}
.hero::after{content:"";position:absolute;inset:0;background:linear-gradient(90deg,rgba(20,30,45,.45),rgba(20,30,45,0) 60%)}
.hero-title{left:112px;top:292px;font-family:'Lora',serif;font-size:50px;line-height:57px;color:var(--white);text-transform:uppercase;z-index:2}
.hero-title b{font-weight:700}
.dot{position:absolute;top:684px;width:7px;height:7px;border-radius:50%;background:var(--white);z-index:2}

/* section headings */
.section-title{left:0;width:1200px;text-align:center;font-family:'Lora',serif;font-size:46px;color:var(--blue-dark);text-transform:uppercase}
.section-title b{font-weight:700;color:var(--blue)}
.lead{left:170px;width:860px;top:884px;text-align:center;font-size:17px;line-height:27px;color:var(--ink)}

.photo{position:absolute}
.feature-icon{position:absolute;left:650px;width:67px;height:67px;background:linear-gradient(135deg,var(--blue),var(--blue-dark));display:flex;align-items:center;justify-content:center}
.feature h3{position:absolute;left:751px;font-size:18px;font-weight:500;color:var(--blue-dark);text-transform:uppercase}
.feature li{position:absolute;left:758px;list-style:none;width:340px;padding-left:19px;font-size:13.5px;line-height:22px;color:var(--muted)}
.feature li svg{position:absolute;left:0;top:5px}

/* services */
.services-band{left:0;top:1598px;width:1200px;height:620px;background:linear-gradient(100deg,var(--blue-pale),#f6f9fc)}
.card{position:absolute;top:1767px;width:303px;height:366px}
.card-label{position:absolute;left:0;right:0;bottom:30px;text-align:center;color:var(--white);font-size:19px;font-weight:700;text-transform:uppercase}
.card-feature{background:linear-gradient(180deg,#1a5f9e,#0a4a8c 60%,#0c3f7a)}
.card-feature h4{position:absolute;top:145px;left:0;right:0;text-align:center;color:var(--white);font-size:19px;font-weight:700}
.card-feature p{position:absolute;top:176px;left:18px;right:18px;text-align:center;color:var(--white);font-size:15.5px;line-height:23px}
.card-feature .learn{position:absolute;left:90px;top:262px;width:123px;height:42px;background:var(--blue-pale);color:var(--blue-dark);font-size:14px;font-weight:500;display:flex;align-items:center;justify-content:center}

/* contact */
.field{position:absolute;background:var(--white);box-shadow:0 4px 14px rgba(0,84,170,.12);font-size:14px;color:#333;padding:0 17px;display:flex;align-items:center}
.field.area{align-items:flex-start;padding-top:18px}

/* footer */
.site-footer{left:0;top:2733px;width:1200px;height:217px;background:linear-gradient(100deg,#0a5aa8,var(--blue-dark) 60%,#0663b0)}
.footer-brand{left:111px;top:2796px;font-family:'Lora',serif;font-size:37px;line-height:46px;color:var(--white);text-transform:uppercase}
.footer-nav{right:112px;top:2841px;display:flex;gap:31px}
.footer-nav a{color:var(--white);font-size:15px;font-weight:700;text-decoration:none;text-transform:uppercase}
.follow{left:865px;top:2794px;color:var(--white);font-size:14px;font-weight:700}
.social{position:absolute;top:2784px;width:34px;height:34px;border-radius:50%;background:rgba(255,255,255,.2)}
.social.first{background:var(--white)}
.copyright{right:112px;top:2884px;color:var(--white);font-size:14px}
</style>
</head>
<body>

<header class="site-header">
  <div class="abs brand">Investment<br>Company</div>
  <nav class="nav">
    <a href="#" class="active" style="left:408px">Home</a>
    <span class="nav-sep" style="left:468px"></span>
    <a href="#" style="left:482px">About Us</a>
    <span class="nav-sep" style="left:571px"></span>
    <a href="#" style="left:586px">Services
      <svg width="10" height="8" viewBox="0 0 10 8" style="margin-left:4px"><path d="M2 2l3 3 3-3" fill="none" stroke="#222" stroke-width="1.5"/></svg></a>
    <span class="nav-sep" style="left:692px"></span>
    <a href="#" style="left:705px">Values</a>
    <span class="nav-sep" style="left:777px"></span>
    <a href="#" style="left:792px">Investments</a>
  </nav>
  <a class="btn" style="left:946px;top:35px;width:135px;height:48px" href="#">Contact Us</a>
</header>

<section class="abs hero" role="img" aria-label="Photo of colleagues shaking hands across a meeting table"></section>
<h1 class="abs hero-title">Empowering<br>Your <b>Financial<br>Future</b></h1>
<a class="btn" style="left:111px;top:485px;width:144px;height:47px;z-index:2">Get Started</a>
<span class="dot" style="left:566px"></span>
<span class="dot" style="left:586px;width:11px;height:11px;top:682px;background:rgba(255,255,255,.55);border:2px solid #fff"></span>
<span class="dot" style="left:608px"></span>
<span class="dot" style="left:629px"></span>

<!-- investments -->
<h2 class="abs section-title" style="top:812px">Our <b>Investments</b></h2>
<p class="abs lead">Lorem ipsum dolor sit amet, consectetur adipiscing elit, sed do eiusmod tempor incididunt ut labore et dolore magna aliqua. Ut enim ad minim veniam, quis nostrud exercitation ullamco laboris nisi ut aliquip ex ea commodo duis aute irure dolor in reprehendea.</p>

<div class="photo" style="left:111px;top:1006px;width:342px;height:386px;background:linear-gradient(140deg,#d9cfd1,#9fbcd2 55%,#dfe8ef)" role="img" aria-label="Photo of hands reviewing charts on a tablet"></div>
<svg class="abs" style="left:172px;top:1396px" width="136" height="46" aria-hidden="true">
  <defs><pattern id="dotgrid" width="12.4" height="10.5" patternUnits="userSpaceOnUse"><circle cx="3" cy="3" r="1.6" fill="#c5c9ce"/></pattern></defs>
  <rect width="136" height="46" fill="url(#dotgrid)"/>
</svg>
<div class="photo" style="left:310px;top:1171px;width:289px;height:306px;background:#fff"></div>
<div class="photo" style="left:318px;top:1179px;width:273px;height:290px;background:linear-gradient(180deg,#a9aca2,#7d8570 55%,#8a6a45)" role="img" aria-label="Photo of plants growing on stacks of coins"></div>

<div class="feature">
  <div class="feature-icon" style="top:1034px"><svg width="40" height="40" viewBox="0 0 40 40" fill="none" stroke="#fff" stroke-width="2"><rect x="6" y="6" width="28" height="18" rx="2"/><path d="M10 20l6-6 5 4 8-8"/><circle cx="15" cy="30" r="5"/><circle cx="27" cy="30" r="4"/></svg></div>
  <h3 style="top:1030px">Lorem ipsum dolor sit amet</h3>
  <ul>
    <li style="top:1064px"><svg width="12" height="12"><path d="M1 6l3 3 7-7" stroke="#0677BA" stroke-width="1.6" fill="none"/></svg>Lorem ipsum dolor sit amet, consectetur adipiscing elit, sed do eiusmod tempor.</li>
    <li style="top:1117px"><svg width="12" height="12"><path d="M1 6l3 3 7-7" stroke="#0677BA" stroke-width="1.6" fill="none"/></svg>Lorem ipsum dolor sit amet, consectetur adipiscing elit, sed do eiusea.</li>
  </ul>
  <div class="feature-icon" style="top:1183px"><svg width="40" height="40" viewBox="0 0 40 40" fill="none" stroke="#fff" stroke-width="2"><circle cx="20" cy="13" r="6"/><path d="M6 28l8-4 6 3 6-3 8 4M10 34l10-4 10 4"/></svg></div>
  <h3 style="top:1178px">Lorem ipsum dolor sit amet</h3>
  <ul>
    <li style="top:1212px"><svg width="12" height="12"><path d="M1 6l3 3 7-7" stroke="#0677BA" stroke-width="1.6" fill="none"/></svg>Lorem ipsum dolor sit amet, consectetur adipiscing elit, sed do eiusmod tempor.</li>
    <li style="top:1265px"><svg width="12" height="12"><path d="M1 6l3 3 7-7" stroke="#0677BA" stroke-width="1.6" fill="none"/></svg>Lorem ipsum dolor sit amet, consectetur adipiscing elit, sed do eiusea.</li>
  </ul>
  <div class="feature-icon" style="top:1329px"><svg width="40" height="40" viewBox="0 0 40 40" fill="none" stroke="#fff" stroke-width="2"><rect x="7" y="22" width="4" height="10"/><rect x="14" y="17" width="4" height="15"/><rect x="21" y="12" width="4" height="20"/><path d="M7 14l8-6 6 4 10-6"/><circle cx="30" cy="28" r="6"/></svg></div>
  <h3 style="top:1325px">Lorem ipsum dolor sit amet</h3>
  <ul>
    <li style="top:1359px"><svg width="12" height="12"><path d="M1 6l3 3 7-7" stroke="#0677BA" stroke-width="1.6" fill="none"/></svg>Lorem ipsum dolor sit amet, consectetur adipiscing elit, sed do eiusmod tempor.</li>
    <li style="top:1412px"><svg width="12" height="12"><path d="M1 6l3 3 7-7" stroke="#0677BA" stroke-width="1.6" fill="none"/></svg>Lorem ipsum dolor sit amet, consectetur adipiscing elit, sed do eiusea.</li>
  </ul>
</div>

<!-- services -->
<section class="abs services-band"></section>
<h2 class="abs section-title" style="top:1669px">Our <b>Services</b></h2>
<div class="card" style="left:111px;background:linear-gradient(160deg,#8a6f55,#c9c2b5 45%,#5a4f45)" role="img" aria-label="Photo of a person pointing at financial reports">
  <div class="card-label">Lorem ipsum dol</div>
</div>
<div class="card card-feature" style="left:448px" role="img" aria-label="Blue toned city skyline with service details">
  <svg class="abs" style="left:124px;top:60px" width="56" height="56" viewBox="0 0 56 56" fill="#fff"><rect x="6" y="34" width="6" height="16"/><rect x="15" y="26" width="6" height="24"/><path d="M24 50V20h-5l8-10 8 10h-5v12" /><circle cx="40" cy="34" r="12" fill="none" stroke="#fff" stroke-width="3"/><text x="40" y="40" font-size="16" font-family="Roboto,sans-serif" font-weight="700" text-anchor="middle">$</text></svg>
  <h4>LOREM IPSUM DOL</h4>
  <p>Lorem ipsum dolor sit amet, consectet adipiscing elit, sed do eiusmod tempor incididunt lab dolorea.</p>
  <div class="learn">LEARN MORE</div>
</div>
<div class="card" style="left:784px;background:linear-gradient(160deg,#5a5e62,#b8a696 45%,#d9d4cf)" role="img" aria-label="Photo of a smiling businesswoman shaking hands">
  <div class="card-label">Lorem ipsum dol</div>
</div>

<!-- contact -->
<h2 class="abs section-title" style="top:2314px">Get in <b>Touch</b></h2>
<div class="field" style="left:166px;top:2411px;width:282px;height:49px">Full Name</div>
<div class="field" style="left:459px;top:2411px;width:282px;height:49px">Phone</div>
<div class="field" style="left:752px;top:2411px;width:282px;height:49px">Email Address</div>
<div class="field area" style="left:166px;top:2472px;width:868px;height:93px">Message</div>
<a class="btn" style="left:520px;top:2584px;width:160px;height:47px">Send Message</a>

<!-- footer -->
<footer class="abs site-footer"></footer>
<div class="abs footer-brand">Investment<br>Company</div>
<div class="abs follow">FOLLOW US:</div>
<span class="social first" style="left:967px"></span>
<span class="social" style="left:1010px"></span>
<span class="social" style="left:1052px"></span>
<nav class="abs footer-nav">
  <a href="#">Home</a><a href="#">About Us</a><a href="#">Services</a><a href="#">Values</a><a href="#">Investments</a><a href="#">Contact Us</a>
</nav>
<div class="abs copyright">Copyright © 2024 All Rights Reserved</div>

</body>
</html>
```